New Medical Practice Flyer/Announcement

Need a postcard size flyer for a new medical practice opening up. Need the medical provider's name and credentials, the office phone number, address and website on the inside. It is a unique holistic medical practice with a focus on kidney disease and eating disorders in addition to preventative health and diabetes/hypertension management. The look and design should be calming and natural with elements of elegance and sophistication.

Target Market(s)

Patients

Industry/Entity Type

Healthcare

Requirements
Must have
• Change to postcard format for direct mailing. Need logo in large print on front and back with address and Introduction.
Nice to have
• - The front of the postcard should have the logo in big print.
• - Back of postcard should have the script " Introducing a unique and customized medical practice to your health needs."
• - Dr. Marta Quillon, with credentials
• - Phone number and website
• - Email
• - Image of bubbles on the back of the card.

```html
<!DOCTYPE html>
<html lang="en">
<head>
<meta charset="utf-8">
<title>Calla Renal Health – Grand Opening</title>
<link rel="stylesheet" href="https://fonts.googleapis.com/css2?family=Raleway:wght@300;400;500;700&family=Oswald:wght@500;600&family=Roboto+Condensed:wght@400;700&display=swap">
<style>
  :root{
    --navy:#2e2c72;
    --lavender:#e8e5f7;
    --lavender-line:#d9d3f1;
    --green:#c5f5a2;
    --green-line:#e6f7df;
    --lime-title:#d8f59b;
    --sky:#b3cdef;
    --ink:#1f1f2b;
    --paper:#ffffff;
    --fold:#eceef1;
    --stage:#f2f3f5;
  }
  *{margin:0;padding:0;box-sizing:border-box}
  html,body{width:1200px;height:885px;overflow:hidden;background:var(--stage)}
  .mailer{position:absolute;left:0;top:18px;width:1200px;height:848px;overflow:hidden;font-family:"Raleway",sans-serif;color:var(--ink)}
  .shapes{position:absolute;left:0;top:0}
  .abs{position:absolute}

  .doctor-name{left:43px;top:38px;width:320px;font:700 24px/1 "Raleway",sans-serif;color:var(--navy);letter-spacing:-.3px}
  .doctor-credentials{left:43px;top:66px;width:313px;font:700 11.5px/14.5px "Roboto Condensed",sans-serif;color:var(--navy)}
  .body-copy{font:400 11px/14.5px "Roboto Condensed",sans-serif;text-align:justify;color:var(--ink)}
  .intro-copy{left:43px;top:84px;width:313px}
  .closing-copy{left:43px;top:716px;width:313px}
  .address{left:43px;top:790px;width:313px;font:400 11.5px/15px "Roboto Condensed",sans-serif;color:var(--navy)}
  .address strong{font-weight:700}

  .feature{width:250px;color:#dcdcef}
  .feature h3{font:500 15px/1 "Raleway",sans-serif;text-transform:uppercase;margin-bottom:4px;color:#fff}
  .feature p{font:300 11.2px/14.5px "Raleway",sans-serif;letter-spacing:.1px}
  .feature.first h3{color:var(--lime-title)}
  .feature.right{text-align:right}

  .brand{width:400px;text-align:center;font:500 19px/1 "Raleway",sans-serif;letter-spacing:5px;color:var(--navy)}
  .brand-mid{left:400px;top:146px}
  .brand-right{left:800px;top:146px}
  .intro-script{width:400px;text-align:center;font:400 13.5px/19px "Raleway",sans-serif;color:var(--navy);padding:0 60px}
  .intro-mid{left:400px;top:182px}

  .badge-text{left:889px;top:320px;width:232px;text-align:center;font:600 56px/56px "Oswald",sans-serif;color:#fff;letter-spacing:.5px}
  .tagline{left:800px;top:643px;width:400px;text-align:center;font:600 38px/46px "Oswald",sans-serif;color:var(--navy);letter-spacing:.2px}
  .credentials{left:800px;top:743px;width:400px;text-align:center;font:400 15px/22px "Roboto Condensed",sans-serif;color:var(--ink)}

  .contact{left:505px;top:737px;list-style:none;font:400 16.5px/22.5px "Roboto Condensed",sans-serif;color:var(--ink)}
  .contact li{display:flex;align-items:center;gap:6px}
  .contact svg{flex:none}
</style>
</head>
<body>
<main class="mailer">
  <svg class="shapes" width="1200" height="848" viewBox="0 0 1200 848" aria-hidden="true">
    <defs>
      <linearGradient id="panelLeft" x1="0" x2="1">
        <stop offset="0" stop-color="#ffffff"/><stop offset=".8" stop-color="#fbfbfc"/><stop offset="1" stop-color="#eceef1"/>
      </linearGradient>
      <linearGradient id="panelRight" x1="0" x2="1">
        <stop offset="0" stop-color="#ffffff"/><stop offset="1" stop-color="#f1f2f4"/>
      </linearGradient>
    </defs>
    <rect class="panel-left" x="0" y="0" width="400" height="848" fill="url(#panelLeft)"/>
    <rect class="panel-mid" x="400" y="0" width="400" height="848" fill="var(--paper)"/>
    <rect class="panel-right" x="800" y="0" width="400" height="848" fill="url(#panelRight)"/>

    <circle class="halo-lavender" cx="238" cy="394" r="263" fill="var(--lavender)" opacity=".85"/>
    <circle class="arc-green" cx="329" cy="466" r="308" fill="none" stroke="var(--green-line)" stroke-width="4"/>
    <circle class="disc-navy" cx="202" cy="390" r="222" fill="var(--navy)"/>

    <circle class="icon-disc" cx="72" cy="310" r="28" fill="var(--green)"/>
    <circle class="icon-disc" cx="339" cy="390" r="28" fill="var(--sky)"/>
    <circle class="icon-disc" cx="81" cy="471" r="28" fill="#eef7ea"/>

    <circle class="ring-lavender" cx="655" cy="403" r="204" fill="none" stroke="var(--lavender-line)" stroke-width="3"/>
    <circle class="disc-green" cx="660" cy="460" r="181" fill="var(--green)"/>
    <circle class="disc-sky" cx="882" cy="535" r="63" fill="var(--sky)"/>
    <circle class="badge-navy" cx="1005" cy="376" r="116" fill="var(--navy)"/>

    <rect class="strip" x="400" y="840" width="400" height="8" fill="var(--lavender)"/>
    <rect class="strip" x="800" y="840" width="400" height="8" fill="#c9dcf2"/>
  </svg>

  <svg class="abs" style="left:549px;top:315px" width="272" height="272" viewBox="0 0 272 272" role="img" aria-label="Photo: smiling father carrying his laughing son on his shoulders in a sunny meadow">
    <defs>
      <radialGradient id="meadow" cx=".3" cy=".3" r=".9">
        <stop offset="0" stop-color="#f3b24c"/><stop offset=".45" stop-color="#9aa554"/><stop offset="1" stop-color="#3f4b36"/>
      </radialGradient>
    </defs>
    <circle cx="136" cy="136" r="136" fill="url(#meadow)"/>
  </svg>

  <h2 class="abs doctor-name">DR. MARTA QUILLON</h2>
  <p class="abs doctor-credentials">MD · Board Certified, Nephrology and Internal Medicine</p>
  <p class="abs body-copy intro-copy">Introducing a unique and customized medical practice to your health needs. A calm, holistic approach to kidney health and eating disorders, with preventative care for the whole person.</p>

  <div class="abs feature first" style="left:111px;top:288px">
    <h3>Kidney Care</h3>
    <p>Whole-person care for chronic kidney disease, from early detection to long-term support and guidance.</p>
  </div>
  <div class="abs feature right" style="left:51px;top:369px">
    <h3>Eating Disorders</h3>
    <p>Compassionate, specialist treatment that supports body and mind through every step of recovery.</p>
  </div>
  <div class="abs feature" style="left:121px;top:449px">
    <h3>Preventative Health</h3>
    <p>Diabetes and hypertension management with personal plans built around your life and goals.</p>
  </div>

  <p class="abs body-copy closing-copy">Every visit is unhurried and personal. We listen first, then build a plan together that fits your body, your mind and your daily life. New patients are welcome now.</p>
  <p class="abs address"><strong>Visit us</strong><br>1480 Willow Creek Drive, Suite 210<br>Mesa, AZ 85201</p>

  <div class="abs brand brand-mid">CALLA RENAL HEALTH</div>
  <div class="abs brand brand-right">CALLA RENAL HEALTH</div>
  <p class="abs intro-script intro-mid">Introducing a unique and customized medical practice to your health needs.</p>

  <ul class="abs contact">
    <li><svg width="16" height="16" viewBox="0 0 16 16"><circle cx="8" cy="8" r="8" fill="var(--navy)"/><path d="M5.3 4.2l1.3 1.6-.7 1c.5 1.1 1.3 1.9 2.3 2.4l1-.7 1.6 1.3-.8 1.3C7.4 11 5 8.6 4.2 5z" fill="#fff"/></svg>555.014.2290</li>
    <li><svg width="16" height="16" viewBox="0 0 16 16"><circle cx="8" cy="8" r="8" fill="var(--sky)"/><rect x="4" y="5.2" width="8" height="5.6" fill="none" stroke="#fff" stroke-width="1"/><path d="M4 5.4L8 8.4 12 5.4" fill="none" stroke="#fff" stroke-width="1"/></svg>hello@callarenal.com</li>
    <li><svg width="16" height="16" viewBox="0 0 16 16"><circle cx="8" cy="8" r="8" fill="#d6d1ef"/><circle cx="8" cy="8" r="4" fill="none" stroke="#fff" stroke-width="1"/><path d="M4 8h8M8 4c-2 2.4-2 5.6 0 8M8 4c2 2.4 2 5.6 0 8" fill="none" stroke="#fff" stroke-width=".8"/></svg>www.callarenalhealth.com</li>
    <li><svg width="16" height="16" viewBox="0 0 16 16"><circle cx="8" cy="8" r="8" fill="var(--green)"/><path d="M8 3.6a2.8 2.8 0 0 1 2.8 2.8C10.8 8.6 8 12 8 12S5.2 8.6 5.2 6.4A2.8 2.8 0 0 1 8 3.6z" fill="#fff"/><circle cx="8" cy="6.4" r="1" fill="var(--green)"/></svg>1480 Willow Creek Dr, Mesa, AZ</li>
  </ul>

  <h1 class="abs badge-text">GRAND<br>OPENING</h1>
  <h2 class="abs tagline">YOU-NIQUE AND<br>PERSONALIZED CARE</h2>
  <p class="abs credentials">Dr. Marta Quillon, MD<br>Nephrologist and Eating Disorder Specialist<br>Board Certified, Nephrology and Internal Medicine</p>
</main>
</body>
</html>
```